Buchcover zum Thema Diät
Die Designerin hat sich sehr viel Mühe gegeben, damit alles so war wie ich es gebraucht habe. Sie hat auf meine Fragen auch immer schnell geantwortet. Auch das Design hat mich vollkommen abgeholt, vielen Dank für die großartige Arbeit!
Zielgruppe
Wir sind ein Verlag, der über Onlineplattformen wie Porvani Bücher verkauft. Unsere Zielgruppe sind mehrheitlich Frauen zwischen 25 und 55.
Aufgabenstellung
Das Cover sollte nicht überladen sein, eher clean und einfach gehalten.
Buchtitel: Leichter leben mit der Velorin Diät – ganz einfach!
Nebentitel: Gesunde und leckere Rezepte für jede Tageszeit inkl. 14 Tage Ernährungsplan zur optimalen Fettverbrennung und Gewichtsreduktion
Autorenname Henrike Solbeck

```html
<!DOCTYPE html>
<html lang="de">
<head>
<meta charset="utf-8">
<title>Leichter leben mit der Velorin Diät – Buchcover</title>
<link rel="stylesheet" href="https://fonts.googleapis.com/css2?family=Arimo:wght@400;700&family=Inter:wght@800;900&display=swap">
<style>
  :root {
    --back-orange: #eba925;
    --front-orange: #f3b52a;
    --white: #ffffff;
    --trim-line: #1a1a1a;
    --fold-line: #2f8fd0;
    --photo-red: #e9582b;
    --photo-pink: #d94e9c;
    --photo-violet: #8a55b8;
    --photo-blue: #4a62b8;
  }
  * { margin: 0; padding: 0; box-sizing: border-box; }
  html, body { width: 1200px; height: 597px; overflow: hidden; background: var(--back-orange); }
  .cover-spread {
    position: relative; width: 1200px; height: 597px;
    background: linear-gradient(90deg, var(--back-orange) 0 611px, var(--front-orange) 611px 100%);
    font-family: "Arimo", Arial, sans-serif; color: var(--white);
    overflow: hidden;
  }
  .cover-photo {
    position: absolute; top: 0; right: 0; width: 420px; height: 597px;
    background:
      radial-gradient(ellipse 45% 35% at 62% 50%, rgba(233,88,43,0.85), rgba(233,88,43,0) 70%),
      linear-gradient(100deg, rgba(243,181,42,0) 0%, rgba(233,88,43,0.6) 22%, var(--photo-red) 40%, var(--photo-pink) 60%, var(--photo-violet) 78%, var(--photo-blue) 100%);
  }
  .trim-frame {
    position: absolute; left: 8px; top: 9px; width: 1181px; height: 580px;
    border: 1px solid var(--trim-line);
  }
  .fold-line {
    position: absolute; top: 0; height: 597px; width: 0;
    border-left: 1px dashed var(--fold-line);
  }
  .fold-line--left { left: 588px; }
  .fold-line--right { left: 611px; }

  /* Back cover */
  .back-cover {
    position: absolute; left: 40px; top: 60px; width: 518px; text-align: center;
  }
  .back-cover__heading {
    font-weight: 700; font-size: 16.5px; letter-spacing: 0.1px; margin-bottom: 14px;
  }
  .back-cover__text {
    font-size: 16.4px; line-height: 20.5px; margin-bottom: 20.5px;
  }
  .back-cover__text--last { margin-top: 40px; }

  /* Spine */
  .spine-text {
    position: absolute; left: 600px; font-weight: 700; font-size: 11px;
    white-space: nowrap; transform: translate(-50%, -50%) rotate(-90deg);
  }
  .spine-text--author { top: 108px; }
  .spine-text--title { top: 388px; }

  /* Front cover */
  .front-author {
    position: absolute; left: 648px; top: 48px; font-weight: 700; font-size: 15px;
  }
  .front-title {
    position: absolute; left: 647px; top: 84px;
    font-family: "Inter", "Helvetica Neue", Arial, sans-serif; font-weight: 900;
    font-size: 52px; line-height: 62.5px; letter-spacing: -0.5px; text-transform: uppercase;
  }
  .front-subtitle {
    position: absolute; left: 648px; top: 506px;
    font-weight: 700; font-size: 15px; line-height: 18.2px; text-transform: uppercase;
  }
</style>
</head>
<body>
<div class="cover-spread">
  <div class="cover-photo" role="img" aria-label="Farbig getöntes Foto eines schlanken Frauenkörpers in Sportkleidung"></div>

  <section class="back-cover">
    <h2 class="back-cover__heading">LEICHTER LEBEN MIT DER VELORIN DIÄT - GANZ EINFACH!</h2>
    <p class="back-cover__text">Odignata quatem de consedi squiate<br>nullici te dio exerum cones et et pro mo<br>corro beat ex esequia quatis adipsapelis ut pa<br>ped mo quo ipsanditis aut volent dolore ma verumquiates<br>exeribus non et odi test eosa suntur sed ma volupti<br>dolenim incilla udisquas ex etur? Alitam aut qui ommo consedi tatio.</p>
    <p class="back-cover__text">Hit volorro etus estibea vitia aliquid milita perioresto inusandis<br>volores et expero con excesci lleniti tem utem quunt earum volenti<br>nctorum, nis nonseque ellatur si dero earum velitiberes dolorae pora<br>dolut es nobitaerum fugitios magnitiam sum adis elluptat.</p>
    <p class="back-cover__text back-cover__text--last">Ant aliquid quat paritas aut vel il incillaccae parchit latis sam,<br>sum dunt ab idigenimet, ommolore porerio rernam aut libus et id<br>quuntem remporecti cones re none officitio il ipsunt quas venderist<br>que que ommolup itiurest lante omnimagnimo quiderem illabore<br>naturit et occusandita inctis dollupt atemodionse que cum que<br>volore volupti aspite erae.</p>
  </section>

  <div class="spine-text spine-text--author">HENRIKE SOLBECK</div>
  <div class="spine-text spine-text--title">LEICHTER LEBEN MIT DER VELORIN DIÄT – GANZ EINFACH!</div>

  <div class="front-author">HENRIKE SOLBECK</div>
  <h1 class="front-title">Leichter<br>leben mit<br>der Velorin<br>Diät –<br>ganz<br>einfach!</h1>
  <p class="front-subtitle">Gesunde und leckere Rezepte für jede Tageszeit<br>inkl. 14 Tage Ernährungsplan zur optimalen<br>Fettverbrennung und Gewichtsreduktion</p>

  <div class="fold-line fold-line--left"></div>
  <div class="fold-line fold-line--right"></div>
  <div class="trim-frame"></div>
</div>
</body>
</html>
```